Moravelt Systems Retractable Banner

Need a design for a retractable banner (approx. 63 inches x 24 inches) Provide us with different raw file types including: ai, png. We may end up ordering a banner that is larger or smaller so please ensure the design provided can be scaled accordingly.
Key Features:
One of the two logos shown below must be displayed (your choice). We can provide other file formats for the logo if needed.
Words that have to be shown:
Your *Data Collection Problems* End Here
Our technology transforms any building into an *IoT Smart Building*
Our *Monitoring and Alerting* capabilities give you full insight and control of your devices and buildings
Please note the words within *(stars) must be accentuated in some way, please use your creative freedom.
A design that fits the look and feel of our brand, as seen in our website here: https://moraveltsys.ca/ is encouraged
Look and feel
Each slider illustrates characteristics of the customer's brand and the style your logo design should communicate.

```html
<!DOCTYPE html>
<html lang="en">
<head>
<meta charset="utf-8">
<title>Moravelt Systems Retractable Banner</title>
<link href="https://fonts.googleapis.com/css2?family=Exo+2:wght@400;600;700&display=swap" rel="stylesheet">
<style>
:root{
  --stage:#c8c8c8;
  --ink:#1d1f22;
  --teal:#1a9fb0;
  --sky-top:#d6f0fb;
  --sky-mid:#ffffff;
  --water:#a9e3f8;
  --city-a:#9ccbe0;
  --city-b:#4a8fae;
}
*{margin:0;padding:0;box-sizing:border-box}
html,body{width:1200px;height:1109px;overflow:hidden;background:var(--stage)}
body{font-family:"Exo 2",sans-serif;color:var(--ink)}
.banner{
  position:absolute;left:401px;top:34px;width:397px;height:1040px;overflow:hidden;
  background:linear-gradient(180deg,var(--sky-top) 0%,var(--sky-mid) 38%,#eef9fd 60%,#dff3fb 100%);
}
.brand{position:absolute;top:50px;left:0;width:100%;display:flex;justify-content:center;align-items:center;gap:10px}
.brand-dot{width:32px;height:32px;border-radius:50%;background:var(--teal)}
.brand-name{font-weight:700;color:var(--ink);font-size:41px;line-height:1;letter-spacing:1px;text-align:left}
.brand-name small{display:block;font-size:12px;letter-spacing:12px;margin-top:3px;padding-left:26px}
.feature-icon{position:absolute;left:170px;width:56px;height:56px}
.copy{position:absolute;left:0;width:100%;text-align:center;font-size:19px;line-height:22.5px}
.accent{color:var(--teal);font-weight:700}
.contact-pill{position:absolute;top:616px;left:154px;width:90px;height:21px;border-radius:11px;
  background:var(--teal);color:#fff;font-size:13.5px;font-weight:600;text-align:center;line-height:21px}
.contacts{position:absolute;top:646px;left:0;width:100%;text-align:center;font-size:16px;line-height:21.5px}
.contacts li{list-style:none;display:flex;justify-content:center;align-items:center;gap:5px}
.contacts svg{width:13px;height:13px;flex:none}
.contacts .phone{font-weight:600}
.city-photo{position:absolute;left:0;top:560px;width:100%;height:480px;
  background:linear-gradient(180deg,rgba(156,203,224,0) 0%,rgba(156,203,224,.45) 32%,var(--city-b) 58%,#6f9a8c 74%,var(--water) 86%,var(--water) 100%)}
</style>
</head>
<body>
<main class="banner">
  <div class="brand">
    <span class="brand-dot"></span>
    <div class="brand-name">MORAVELT<small>SYSTEMS</small></div>
  </div>

  <svg class="feature-icon" style="top:147px" viewBox="0 0 56 56">
    <circle cx="28" cy="28" r="27" fill="var(--teal)" stroke="#7fd3df" stroke-width="2"/>
    <g fill="none" stroke="#fff" stroke-width="1.5">
      <ellipse cx="28" cy="21" rx="7" ry="3"/>
      <path d="M21 21v13c0 1.7 3.1 3 7 3s7-1.3 7-3V21M21 27.5c0 1.7 3.1 3 7 3s7-1.3 7-3"/>
      <ellipse cx="28" cy="28" rx="16" ry="7" transform="rotate(-30 28 28)"/>
    </g>
  </svg>
  <p class="copy" style="top:212px">Your <span class="accent">Data Collection</span><br><span class="accent">Problems</span> End Here</p>

  <svg class="feature-icon" style="top:274px" viewBox="0 0 56 56">
    <circle cx="28" cy="28" r="27" fill="var(--teal)" stroke="#7fd3df" stroke-width="2"/>
    <g fill="none" stroke="#fff" stroke-width="1.5">
      <path d="M14 40h28M17 40V28h6v12M24 40V18h8v22M33 40V25h6v15"/>
      <path d="M26 22h4M26 26h4M26 30h4M26 34h4"/>
      <circle cx="28" cy="13" r="1.5"/>
    </g>
  </svg>
  <p class="copy" style="top:338px">Our technology<br>transforms any building into an<br><span class="accent">IoT Smart Building</span></p>

  <svg class="feature-icon" style="top:420px" viewBox="0 0 56 56">
    <circle cx="28" cy="28" r="27" fill="var(--teal)" stroke="#7fd3df" stroke-width="2"/>
    <g fill="none" stroke="#fff" stroke-width="1.5">
      <rect x="14" y="16" width="28" height="19" rx="1.5"/>
      <path d="M24 39h8M28 35v4M18 31l6-6 5 4 8-8"/>
      <path d="M19 29v-3M23 29v-6M27 29v-4"/>
    </g>
  </svg>
  <p class="copy" style="top:483px">Our <span class="accent">Monitoring and Alerting</span><br>capabilities give you full insight<br>and control of your devices<br>and buildings</p>

  <div class="city-photo" role="img" aria-label="Photo of a waterfront city skyline with a tall observation tower and glass high-rise towers, framed by light blue water shapes at the bottom"></div>

  <div class="contact-pill">Contact Us</div>
  <ul class="contacts">
    <li class="phone"><svg viewBox="0 0 14 14"><circle cx="7" cy="7" r="6" fill="none" stroke="var(--teal)"/><path d="M5 4.5l1 1.5-.7.8a4 4 0 0 0 1.9 1.9l.8-.7 1.5 1-.6 1A5 5 0 0 1 4 5.1z" fill="var(--teal)"/></svg><span>+1 (888) 555-0142</span></li>
    <li><svg viewBox="0 0 14 14"><circle cx="7" cy="7" r="6" fill="none" stroke="var(--teal)"/><circle cx="7" cy="7" r="3" fill="var(--teal)"/></svg><span>www.<span class="accent">moraveltsys</span>.ca</span></li>
    <li><svg viewBox="0 0 14 14"><circle cx="7" cy="7" r="6" fill="none" stroke="var(--teal)"/><rect x="4" y="5" width="6" height="4" fill="var(--teal)"/></svg><span>sales@<span class="accent">moraveltsys</span>.ca</span></li>
  </ul>
</main>
</body>
</html>
```